Sticker mit Text
Zielgruppe
Buchverkauf
Aufgabenstellung
Das Design soll als Sticker in Pakete geklebt werden. Hierfür verwenden wir Die Cut Sticker von Klebfuchs in einer Formatgröße von etwa 10x10cm. https://www.klebfuchs.example/products/die-cut-stickers
Auf dem Sticker soll folgender Text enthalten sein:
Haben Sie es gewusst? Es gibt nur 4 giftige Vogelarten.
Der Pitohui ist einer von ihnen. Er ist giftig, weil er giftige Käfer frisst. Je mehr er davon verspeist, desto giftiger wird er.
Was manche Käufer bei Kaufwelt vielleicht auch nicht wissen, dass sich ein Verkäufer prima durch eine Sterne-Bewertung unterstützen lässt. Probieren Sie es aus. Wenden Sie hierfür vorsichtig die Feder des Pitohui!
Von der Umrandung des Stickers sollte man einen Vogel erkennen können. Ggf. lässt sich ein Vogel aber auch in den Sticker integrieren.

```html
<!DOCTYPE html>
<html lang="de">
<head>
<meta charset="utf-8">
<title>Pitohui Sticker</title>
<link href="https://fonts.googleapis.com/css2?family=Anton&family=Roboto+Condensed:wght@400;500&display=swap" rel="stylesheet">
<style>
  :root {
    --bg: #e3e2e0;
    --paper: #ffffff;
    --ink: #111111;
    --orange: #ee7d0f;
    --shade: rgba(0,0,0,0.12);
  }
  html, body {
    margin: 0;
    padding: 0;
    width: 848px;
    height: 1200px;
    overflow: hidden;
    background: var(--bg);
  }
  .sticker {
    position: absolute;
    left: 74px;
    top: 230px;
    width: 700px;
    height: 720px;
  }
  .sticker-shape {
    position: absolute;
    inset: 0;
    width: 700px;
    height: 720px;
    overflow: visible;
  }
  .pitohui {
    position: absolute;
    left: 40px;
    top: 30px;
    width: 250px;
    height: 250px;
    border-radius: 50%;
    background: radial-gradient(circle at 55% 40%, #2a2a2a 0%, var(--ink) 70%);
    border: 10px solid var(--paper);
    box-sizing: border-box;
    box-shadow: 0 2px 6px var(--shade);
    transform: rotate(-6deg);
  }
  .copy {
    position: absolute;
    left: 150px;
    top: 260px;
    width: 440px;
    transform: rotate(-4deg);
    text-align: center;
    font-family: "Roboto Condensed", sans-serif;
    color: var(--ink);
  }
  .band {
    display: inline-block;
    background: var(--ink);
    color: var(--orange);
    font-family: "Anton", sans-serif;
    text-transform: uppercase;
    letter-spacing: 0.5px;
    line-height: 1.1;
    padding: 4px 12px;
  }
  .band--title { font-size: 28px; margin-left: 120px; }
  .fact {
    font-size: 19px;
    line-height: 1.25;
    margin: 6px 0 14px;
  }
  .lead {
    font-size: 19px;
    line-height: 1.25;
    margin: 0 0 6px;
  }
  .claim { text-align: left; }
  .band--small { font-size: 21px; }
  .band--large { font-size: 32px; margin-left: 30px; }
  .band--mid { font-size: 31px; }
  .band--note {
    background: var(--ink);
    color: var(--paper);
    font-family: "Roboto Condensed", sans-serif;
    font-weight: 500;
    font-size: 18px;
    text-transform: none;
    text-align: center;
    padding: 4px 14px 8px;
    margin-left: 40px;
  }
</style>
</head>
<body>
  <div class="sticker">
    <svg class="sticker-shape" viewBox="0 0 700 720" aria-hidden="true">
      <g transform="rotate(-6 350 380)">
        <polygon points="350,20 444,251 692,269 502,429 562,671 350,540 138,671 198,429 8,269 256,251"
                 fill="var(--shade)" transform="translate(3 4)"/>
        <polygon points="350,20 444,251 692,269 502,429 562,671 350,540 138,671 198,429 8,269 256,251"
                 fill="var(--paper)"/>
      </g>
    </svg>

    <div class="pitohui" role="img" aria-label="Illustration eines runden schwarzen Pitohui-Vogels mit orangem Flügel und orangem Auge"></div>

    <div class="copy">
      <div class="band band--title">Haben Sie es gewusst?</div>
      <p class="fact">Es gibt nur 4 giftige Vogelarten. Der Pitohui ist einer von ihnen. Er ist giftig, weil er giftige Käfer frisst. Je mehr er davon verspeist, desto giftiger wird er.</p>
      <p class="lead">Was manche Käufer<br>bei Kaufwelt vielleicht auch nicht wissen,</p>
      <div class="claim">
        <div class="band band--small">Dass sich ein Verkäufer prima durch</div><br>
        <div class="band band--large">Eine Sterne-Bewertung</div><br>
        <div class="band band--mid">Unterstützen lässt.</div><br>
        <div class="band band--note">Probieren Sie es aus. Wenden Sie hierfür<br>vorsichtig die Feder des Pitohui!</div>
      </div>
    </div>
  </div>
</body>
</html>
```